Business Card Re-Design

Consulting Company: To build a high performance organization, you need great leaders at all levels throughout your organization. The Northvale Talent Growth Studio engages, inspires, and educates current and future leaders to step beyond the ordinary and deliver exceptional results. This new breed of leaders will motivate your staff to leave the safety of complacency behind and come together to build an extraordinary organization. The current trend has been to ask our people to do more with fewer resources. People have been stepping up to the challenge, but more is required to ensure success with a new work paradigm. We work with your management team to build a successful strategy that will make your organization more effective. NTGS then supports your management team by providing a comprehensive set of proven services to empower your entire organization to successfully execute new strategies.Let NTGS help you optimize your organization’s individual and team performance today!

Target Market(s)

Federal, State and Local Government / Non profit

Industry/Entity Type

Management Consulting

Contact Information for Business Card

NTGS, inc (Northvale Talent Growth Studio) Optimizing Individual and Organizational Performance

Colors
fee18a
ec1f27
474747
fbf289

Requirements
Must have
• Professional and high quality feel

```html
<!DOCTYPE html>
<html lang="en">
<head>
<meta charset="utf-8">
<title>NTGS Business Card</title>
<link href="https://fonts.googleapis.com/css2?family=Cinzel:wght@400;600;700&family=Crimson+Text:wght@400&display=swap" rel="stylesheet">
<style>
  :root {
    --stage: #2a2622;
    --card-black: #0b0b0b;
    --card-charcoal: #1c1c1c;
    --gold: #fee18a;
    --gold-pale: #e8d79a;
    --gold-edge: #c9b877;
    --red: #ec1f27;
    --red-deep: #c8161d;
    --white: #ffffff;
    --grey: #474747;
  }
  * { margin: 0; padding: 0; box-sizing: border-box; }
  html, body {
    width: 1200px;
    height: 1022px;
    overflow: hidden;
    background: var(--stage);
  }
  .business-card {
    position: absolute;
    left: 100px;
    top: 225px;
    width: 1000px;
    height: 572px;
    background: linear-gradient(150deg, var(--card-charcoal) 0%, var(--card-black) 55%, #050505 100%);
    overflow: hidden;
    box-shadow: 0 20px 50px rgba(0,0,0,0.5);
  }
  .divider-line {
    position: absolute;
    left: 700px;
    top: 0;
    width: 1.5px;
    height: 100%;
    background: var(--white);
    opacity: 0.85;
  }
  .edge-band {
    position: absolute;
    left: 0;
    bottom: 0;
    width: 100%;
    height: 100%;
  }
  .identity {
    position: absolute;
    left: 170px;
    top: 70px;
    width: 500px;
  }
  .brand-name {
    font-family: "Cinzel", serif;
    font-weight: 600;
    font-size: 76px;
    line-height: 1;
    color: var(--gold);
    letter-spacing: 4px;
    display: flex;
    align-items: center;
    gap: 18px;
  }
  .brand-name .brand-square {
    width: 18px;
    height: 18px;
    background: var(--gold);
  }
  .company-name {
    margin-top: 14px;
    font-family: "Cinzel", serif;
    font-weight: 400;
    font-size: 17px;
    letter-spacing: 1.5px;
    color: var(--white);
    white-space: nowrap;
  }
  .company-name .accent { color: var(--gold); }
  .person-name {
    margin-top: 22px;
    font-family: "Cinzel", serif;
    font-weight: 700;
    font-size: 33px;
    letter-spacing: 1px;
    color: var(--white);
    white-space: nowrap;
  }
  .person-title {
    margin-top: 4px;
    font-family: "Cinzel", serif;
    font-weight: 400;
    font-size: 22px;
    color: var(--gold);
    letter-spacing: 1px;
  }
  .contact-icons {
    margin-top: 18px;
    display: flex;
    gap: 12px;
  }
  .contact-icons svg { width: 16px; height: 16px; }
  .contact-list {
    margin-top: 8px;
    list-style: none;
    font-family: "Crimson Text", serif;
    font-size: 24px;
    line-height: 1.3;
    color: var(--white);
  }
</style>
</head>
<body>
  <section class="business-card" aria-label="NTGS business card front">
    <div class="divider-line"></div>

    <svg class="edge-band" viewBox="0 0 1000 572" preserveAspectRatio="none" aria-hidden="true">
      <rect x="0" y="548" width="1000" height="24" fill="var(--gold-pale)"/>
      <rect x="0" y="548" width="1000" height="3" fill="var(--gold-edge)"/>
      <polygon points="470,548 520,478 1000,478 1000,548" fill="var(--red)"/>
      <polygon points="470,548 520,478 526,478 478,548" fill="var(--red-deep)"/>
    </svg>

    <div class="identity">
      <div class="brand-name"><span>NTGS</span><span class="brand-square"></span></div>
      <p class="company-name">Northvale Talent <span class="accent">Growth Studio</span></p>
      <h1 class="person-name">DANIEL R. WHITCOMBE</h1>
      <p class="person-title">PRESIDENT/CEO</p>
      <div class="contact-icons" aria-hidden="true">
        <svg viewBox="0 0 16 16"><path d="M4 1.5 L6.5 4.5 L5 6 C6 8.2 7.8 10 10 11 L11.5 9.5 L14.5 12 L12.5 14.5 C6.5 14 2 9.5 1.5 3.5 Z" fill="var(--gold)"/></svg>
        <svg viewBox="0 0 16 16"><rect x="1.5" y="3.5" width="13" height="9" fill="none" stroke="var(--gold)" stroke-width="1.4"/><path d="M1.5 3.5 L8 9 L14.5 3.5" fill="none" stroke="var(--gold)" stroke-width="1.4"/></svg>
        <svg viewBox="0 0 16 16"><circle cx="8" cy="8" r="6.3" fill="none" stroke="var(--gold)" stroke-width="1.4"/><ellipse cx="8" cy="8" rx="2.6" ry="6.3" fill="none" stroke="var(--gold)" stroke-width="1.1"/><line x1="1.7" y1="8" x2="14.3" y2="8" stroke="var(--gold)" stroke-width="1.1"/></svg>
      </div>
      <ul class="contact-list">
        <li>301-555-0142</li>
        <li>dwhitcombe@ntgsinc.com</li>
        <li>www.ntgsinc.com</li>
      </ul>
    </div>
  </section>
</body>
</html>
```